Numbrella : This is a Puzzle and This is not a Puzzle

Numbrella is a new addictive way to play Sudoku (see description on the attached document).
We would like your help in developing a design for the playscreen of the game (a mock-up is in the attached document)
The winner will be entrusted with the work of the complete design of the application (home screen, configuration screen, etc.) in a specific contract.
Thank you from Paris France.
Best.
Anselme

```html
<!DOCTYPE html>
<html lang="en">
<head>
<meta charset="utf-8">
<title>Numbrella – Play Screen</title>
<link href="https://fonts.googleapis.com/css2?family=Nunito:wght@500;600&display=swap" rel="stylesheet">
<style>
  :root{
    --page:#cbe4fb;
    --panel:#0b6cd3;
    --button:#3d8fe6;
    --board:#ffffff;
    --badge:#8dc1f1;
    --tile:#cfe5fb;
    --tile-text:#3d8fe6;
    --icon-left:#ffe600;
    --icon-right:#ffffff;
    --c-red:#ff0000; --c-mag:#ff00ff; --c-yel:#ffff00; --c-gry:#c0c0c0;
    --c-blk:#000000; --c-blu:#0000c0; --c-gld:#c8960a; --c-grn:#00ff00; --c-cyn:#00ffff;
    --soft-text:#3d8fe6;
  }
  *{box-sizing:border-box;margin:0;padding:0}
  html,body{width:1200px;height:1200px;overflow:hidden;background:var(--page);font-family:"Nunito",sans-serif}
  .play-screen{position:absolute;left:56px;top:349px;width:906px;height:418px;background:var(--panel);border-radius:30px;transform:scale(1.2);transform-origin:0 0}
  .rating{position:absolute;top:14px;width:21px;height:111px;border-radius:3px}
  .rating--player{left:58px;background:#fff}
  .rating--target{left:88px;background:#5aa2ea}
  .rating svg{display:block}
  .btn{position:absolute;width:51px;height:51px;border-radius:8px;background:var(--button);display:flex;align-items:center;justify-content:center}
  .btn svg{width:32px;height:32px}
  .side-left .btn{left:58px}
  .side-right .btn{left:797px}
  .board{position:absolute;left:135px;top:0;width:636px;height:418px;background:var(--board);border-radius:14px}
  .groups{position:absolute;top:14px;display:flex;flex-direction:column;gap:9px}
  .group{display:flex;flex-direction:column;gap:5px}
  .legend-row{display:flex;align-items:flex-end;height:38px}
  .badge{width:26px;height:22px;border-radius:4px;background:var(--badge);color:#fff;font-size:14px;font-weight:600;display:flex;align-items:center;justify-content:center;margin-bottom:-4px}
  .swatch{width:38px;height:38px;border-radius:4px;margin-left:4px}
  .legend-colors{left:22px}
  .legend-digits{left:546px}
  .legend-digits .badge{margin-left:5px}
  .digit-tile{width:38px;height:38px;border-radius:4px;background:var(--tile);color:var(--tile-text);font-size:20px;display:flex;align-items:center;justify-content:center}
  .grid{position:absolute;left:123px;top:14px;display:grid;grid-template-columns:repeat(3,124px);gap:9px}
  .block{display:grid;grid-template-columns:repeat(3,38px);gap:5px}
  .cell{width:38px;height:38px;border-radius:4px;color:#fff;font-size:20px;font-weight:500;display:flex;align-items:center;justify-content:center}
  .R{background:var(--c-red)} .M{background:var(--c-mag)} .Y{background:var(--c-yel);color:var(--soft-text)}
  .G{background:var(--c-gry)} .K{background:var(--c-blk)} .B{background:var(--c-blu)}
  .O{background:var(--c-gld)} .L{background:var(--c-grn)} .C{background:var(--c-cyn);color:var(--soft-text)}
</style>
</head>
<body>
<main class="play-screen" aria-label="Numbrella play screen">

  <div class="side-left">
    <div class="rating rating--player" aria-label="Player rating">
      <svg width="21" height="111" viewBox="0 0 21 111">
        <g fill="#b9dcfa"><path id="st" d="M10.5 5l2 4.5 4.8.4-3.7 3.2 1.1 4.7-4.2-2.5-4.2 2.5 1.1-4.7-3.7-3.2 4.8-.4z"/>
        <use href="#st" y="17"/><use href="#st" y="34"/></g>
        <g fill="#ff1a1a"><use href="#st" y="51"/><use href="#st" y="68"/></g>
        <circle cx="10.5" cy="99" r="8" fill="#0b6cd3"/><use href="#st" y="87.5" fill="#fff" transform="translate(2.6 20.6) scale(.75)"/>
      </svg>
    </div>
    <div class="rating rating--target" aria-label="Target rating">
      <svg width="21" height="111" viewBox="0 0 21 111">
        <g fill="#b9dcfa"><use href="#st"/><use href="#st" y="17"/><use href="#st" y="34"/><use href="#st" y="51"/></g>
        <use href="#st" y="68" fill="#ffe600"/>
        <circle cx="10.5" cy="99" r="8" fill="#fff"/><use href="#st" y="87.5" fill="#5aa2ea" transform="translate(2.6 20.6) scale(.75)"/>
      </svg>
    </div>

    <div class="btn" style="top:173px" aria-label="Previous">
      <svg viewBox="0 0 32 32" fill="var(--icon-left)"><path d="M15 8v16L4 16zM28 8v16L17 16z"/></svg>
    </div>
    <div class="btn" style="top:233px" aria-label="Reveal">
      <svg viewBox="0 0 32 32" fill="none" stroke="var(--icon-left)" stroke-width="2.5"><rect x="4" y="4" width="9" height="9"/><rect x="4" y="18" width="9" height="9"/><rect x="18" y="18" width="9" height="9"/><path d="M16 9c4-5 10-5 14 0-4 5-10 5-14 0z" stroke-width="2"/><circle cx="23" cy="9" r="2" fill="var(--icon-left)" stroke="none"/></svg>
    </div>
    <div class="btn" style="top:293px" aria-label="Erase">
      <svg viewBox="0 0 32 32" fill="var(--icon-left)"><path d="M18 4l10 10-9 9H9l-5-5z"/><path d="M4 27h24" stroke="var(--icon-left)" stroke-width="3"/></svg>
    </div>
    <div class="btn" style="top:353px" aria-label="Hint">
      <svg viewBox="0 0 32 32" fill="var(--icon-left)"><path d="M16 3a9 9 0 0 0-5 16.5V23h10v-3.5A9 9 0 0 0 16 3z"/><rect x="11" y="25" width="10" height="2.5" rx="1"/><rect x="13" y="29" width="6" height="2" rx="1"/></svg>
    </div>
  </div>

  <section class="board">
    <div class="groups legend-colors">
      <div class="group">
        <div class="legend-row"><span class="badge">1</span><span class="swatch R"></span></div>
        <div class="legend-row"><span class="badge">4</span><span class="swatch M"></span></div>
        <div class="legend-row"><span class="badge">4</span><span class="swatch Y"></span></div>
      </div>
      <div class="group">
        <div class="legend-row"><span class="badge">2</span><span class="swatch G"></span></div>
        <div class="legend-row"><span class="badge">6</span><span class="swatch K"></span></div>
        <div class="legend-row"><span class="badge">5</span><span class="swatch B"></span></div>
      </div>
      <div class="group">
        <div class="legend-row"><span class="badge">7</span><span class="swatch O"></span></div>
        <div class="legend-row"><span class="badge">5</span><span class="swatch L"></span></div>
        <div class="legend-row"><span class="badge">2</span><span class="swatch C"></span></div>
      </div>
    </div>

    <div class="grid">
      <div class="block"><span class="cell B">1</span><span class="cell C">8</span><span class="cell O">2</span><span class="cell G">3</span><span class="cell K">5</span><span class="cell M">9</span><span class="cell R">6</span><span class="cell L">7</span><span class="cell Y">4</span></div>
      <div class="block"><span class="cell R">1</span><span class="cell G">8</span><span class="cell K">2</span><span class="cell C">3</span><span class="cell L">5</span><span class="cell Y">9</span><span class="cell M">6</span><span class="cell O">7</span><span class="cell B">4</span></div>
      <div class="block"><span class="cell M">1</span><span class="cell Y">8</span><span class="cell L">2</span><span class="cell R">3</span><span class="cell B">5</span><span class="cell O">9</span><span class="cell C">6</span><span class="cell G">7</span><span class="cell K">4</span></div>
      <div class="block"><span class="cell C">1</span><span class="cell R">8</span><span class="cell B">2</span><span class="cell M">3</span><span class="cell G">5</span><span class="cell K">9</span><span class="cell Y">6</span><span class="cell O">7</span><span class="cell L">4</span></div>
      <div class="block"><span class="cell O">1</span><span class="cell K">8</span><span class="cell M">2</span><span class="cell Y">3</span><span class="cell R">5</span><span class="cell L">9</span><span class="cell G">6</span><span class="cell B">7</span><span class="cell C">4</span></div>
      <div class="block"><span class="cell Y">1</span><span class="cell L">8</span><span class="cell G">2</span><span class="cell B">3</span><span class="cell O">5</span><span class="cell C">9</span><span class="cell K">6</span><span class="cell M">7</span><span class="cell R">4</span></div>
      <div class="block"><span class="cell K">1</span><span class="cell B">8</span><span class="cell G">2</span><span class="cell O">3</span><span class="cell Y">5</span><span class="cell C">9</span><span class="cell L">6</span><span class="cell M">7</span><span class="cell R">4</span></div>
      <div class="block"><span class="cell L">1</span><span class="cell Y">8</span><span class="cell R">2</span><span class="cell K">3</span><span class="cell M">5</span><span class="cell G">9</span><span class="cell B">6</span><span class="cell C">7</span><span class="cell O">4</span></div>
      <div class="block"><span class="cell O">1</span><span class="cell C">8</span><span class="cell M">2</span><span class="cell L">3</span><span class="cell R">5</span><span class="cell B">9</span><span class="cell G">6</span><span class="cell K">7</span><span class="cell Y">4</span></div>
    </div>

    <div class="groups legend-digits">
      <div class="group">
        <div class="legend-row"><span class="digit-tile">1</span><span class="badge">1</span></div>
        <div class="legend-row"><span class="digit-tile">2</span><span class="badge">4</span></div>
        <div class="legend-row"><span class="digit-tile">3</span><span class="badge">4</span></div>
      </div>
      <div class="group">
        <div class="legend-row"><span class="digit-tile">4</span><span class="badge">2</span></div>
        <div class="legend-row"><span class="digit-tile">5</span><span class="badge">6</span></div>
        <div class="legend-row"><span class="digit-tile">6</span><span class="badge">5</span></div>
      </div>
      <div class="group">
        <div class="legend-row"><span class="digit-tile">7</span><span class="badge">7</span></div>
        <div class="legend-row"><span class="digit-tile">8</span><span class="badge">5</span></div>
        <div class="legend-row"><span class="digit-tile">9</span><span class="badge">2</span></div>
      </div>
    </div>
  </section>

  <div class="side-right">
    <div class="btn" style="top:14px" aria-label="Home">
      <svg viewBox="0 0 32 32" fill="var(--icon-right)"><path d="M16 4L2 16h4v12h7v-8h6v8h7V16h4z"/></svg>
    </div>
    <div class="btn" style="top:74px" aria-label="Restart 60 seconds">
      <svg viewBox="0 0 32 32"><path d="M9 7.5A12 12 0 1 1 5 14" fill="none" stroke="var(--icon-right)" stroke-width="2.5"/><path d="M4 4v8h8z" fill="var(--icon-right)"/><text x="16.5" y="21" font-size="10" font-weight="600" text-anchor="middle" fill="var(--icon-right)" font-family="Nunito, sans-serif">60</text></svg>
    </div>
    <div class="btn" style="top:173px" aria-label="Next">
      <svg viewBox="0 0 32 32" fill="var(--icon-right)"><path d="M4 8v16l11-8zM17 8v16l11-8z"/></svg>
    </div>
    <div class="btn" style="top:233px" aria-label="Reveal">
      <svg viewBox="0 0 32 32" fill="none" stroke="var(--icon-right)" stroke-width="2.5"><rect x="4" y="4" width="9" height="9"/><rect x="4" y="18" width="9" height="9"/><rect x="18" y="18" width="9" height="9"/><path d="M16 9c4-5 10-5 14 0-4 5-10 5-14 0z" stroke-width="2"/><circle cx="23" cy="9" r="2" fill="var(--icon-right)" stroke="none"/></svg>
    </div>
    <div class="btn" style="top:293px" aria-label="Erase">
      <svg viewBox="0 0 32 32" fill="var(--icon-right)"><path d="M18 4l10 10-9 9H9l-5-5z"/><path d="M4 27h24" stroke="var(--icon-right)" stroke-width="3"/></svg>
    </div>
    <div class="btn" style="top:353px" aria-label="Hint">
      <svg viewBox="0 0 32 32" fill="none" stroke="var(--icon-right)" stroke-width="2.5"><path d="M16 4a8.5 8.5 0 0 0-4.5 15.7V23h9v-3.3A8.5 8.5 0 0 0 16 4z"/><path d="M12 27h8M14 30h4"/></svg>
    </div>
  </div>

</main>
</body>
</html>
```